Dulwick Medical

Need smart and sleek business cards design for my medical distribution company. use logos attached.

add my details

Harriet Colbeck
Director/Sales Agent
harriet@dulwickmedical.com.au
0461 835 207

```html
<!DOCTYPE html>
<html lang="en">
<head>
<meta charset="utf-8">
<title>Dulwick Medical — Business Cards</title>
<link rel="stylesheet" href="https://fonts.googleapis.com/css2?family=Lato:wght@400;700;900&display=swap">
<style>
  :root {
    --navy: #03215a;
    --blue: #1f73a3;
    --paper: #f4f4f4;
    --stage: #e5e5e7;
    --ink: #2b2b2b;
    --white: #ffffff;
  }
  * { margin: 0; padding: 0; box-sizing: border-box; }
  html, body {
    width: 1200px; height: 918px; overflow: hidden;
    background: var(--stage);
    font-family: "Lato", Arial, sans-serif;
  }
  .sheet {
    width: 1200px; height: 918px;
    display: flex; align-items: center; justify-content: center; gap: 44px;
  }
  .card {
    width: 540px; height: 330px; position: relative; overflow: hidden;
    box-shadow: 0 10px 28px rgba(0,0,0,0.14);
  }
  /* Front: contact side */
  .card--front { background: var(--paper); }
  .front__mark {
    position: absolute; left: 58px; bottom: 0;
    width: 120px; height: 120px; background: var(--blue);
  }
  .contact {
    position: absolute; right: 44px; top: 92px; text-align: right;
  }
  .contact__name {
    font-weight: 900; font-size: 25px; letter-spacing: 0.5px;
    color: var(--navy); text-transform: uppercase;
  }
  .contact__role {
    font-size: 15px; color: var(--blue); margin-top: 2px; letter-spacing: 0.3px;
  }
  .contact__rule {
    width: 56px; height: 1.5px; background: var(--navy);
    margin: 14px 0 12px auto;
  }
  .contact__line {
    display: flex; align-items: center; justify-content: flex-end; gap: 8px;
    font-size: 14px; color: var(--ink); margin-bottom: 8px;
  }
  .contact__icon { width: 13px; height: 13px; fill: var(--blue); }
  /* Back: brand side */
  .card--back {
    background: var(--navy);
    display: flex; align-items: center; justify-content: center; gap: 16px;
  }
  .brand__square { width: 30px; height: 30px; background: var(--blue); }
  .brand__name {
    font-weight: 700; font-size: 36px; color: var(--white);
    letter-spacing: 3px; text-transform: uppercase;
  }
</style>
</head>
<body>
<main class="sheet">
  <section class="card card--front" aria-label="Business card front">
    <div class="front__mark" aria-hidden="true"></div>
    <div class="contact">
      <h1 class="contact__name">Harriet Colbeck</h1>
      <p class="contact__role">Director / Sales Agent</p>
      <div class="contact__rule"></div>
      <p class="contact__line">0461 835 207
        <svg class="contact__icon" viewBox="0 0 24 24" aria-hidden="true"><path d="M6.6 10.8a15.1 15.1 0 0 0 6.6 6.6l2.2-2.2c.3-.3.7-.4 1-.2 1.1.4 2.3.6 3.6.6.6 0 1 .4 1 1V20c0 .6-.4 1-1 1A17 17 0 0 1 3 4c0-.6.4-1 1-1h3.5c.6 0 1 .4 1 1 0 1.3.2 2.5.6 3.6.1.3 0 .7-.2 1z"/></svg>
      </p>
      <p class="contact__line">harriet@dulwickmedical.com.au
        <svg class="contact__icon" viewBox="0 0 24 24" aria-hidden="true"><path d="M2 5h20v14H2z M2 5l10 8 10-8" stroke="#f4f4f4" stroke-width="1.5"/></svg>
      </p>
    </div>
  </section>
  <section class="card card--back" aria-label="Business card back">
    <div class="brand__square" aria-hidden="true"></div>
    <p class="brand__name">Dulwick Medical</p>
  </section>
</main>
</body>
</html>
```